Modern wordpress-enabled design wanted for translations agency serving large corporations

We are a translation agency and we only work for corporate clients and not private individuals. We are currently using the Larvesk wordpress theme and an upload feature called trobanex. It is important that prospective clients can upload their file. So we need a cool design for that kind of feature. We offer different kinds of translations tailored to the needs or global corporations. Corporate communications translations, legal translations, financial translations, healthcare translations, financial translations, audit translations.

```html
<!DOCTYPE html>
<html lang="en">
<head>
<meta charset="utf-8">
<title>Trobanex Translations</title>
<link href="https://fonts.googleapis.com/css2?family=Oswald:wght@400;500;700&family=Open+Sans:wght@400;600;700&display=swap" rel="stylesheet">
<style>
:root{
  --orange:#f26b21;
  --orange-soft:#f79a3a;
  --amber:#f4a623;
  --green:#6cb33f;
  --teal:#1b8a9a;
  --blue:#1e7bc4;
  --ink:#333;
  --muted:#777;
  --line:#e2e2e2;
  --panel:#f2f2f2;
  --white:#fff;
}
*{margin:0;padding:0;box-sizing:border-box}
html,body{width:756px;height:1200px;overflow:hidden;background:var(--white)}
body{font-family:"Open Sans",sans-serif;color:var(--ink);font-size:9px;line-height:1.5;position:relative}
.heading{font-family:"Oswald",sans-serif;text-transform:uppercase}

/* header */
.site-header{height:75px;position:relative;border-bottom:1px solid var(--line)}
.brand{position:absolute;left:40px;top:22px}
.brand-name{font-family:"Open Sans",sans-serif;font-weight:700;font-size:17px;line-height:1;color:var(--ink);white-space:nowrap}
.top-actions{position:absolute;right:40px;top:12px;display:flex;gap:8px}
.top-actions span{font-size:7px;color:#fff;padding:4px 10px;font-weight:600;text-transform:uppercase}
.btn-blue{background:var(--blue)}
.btn-orange{background:var(--orange)}
.main-nav{position:absolute;right:40px;top:48px;display:flex}
.main-nav a{font-family:"Oswald",sans-serif;font-size:9px;color:var(--ink);text-decoration:none;padding:5px 10px;text-transform:uppercase}
.main-nav a.active{background:var(--orange);color:#fff}

/* hero */
.hero{position:absolute;top:76px;left:0;width:756px;height:290px;background:linear-gradient(90deg,#9a9a9a 0%,#c9c9c9 45%,#ececec 70%,#f5f5f5 100%)}
.hero-photo{position:absolute;left:90px;top:0;width:340px;height:290px;background:linear-gradient(180deg,#8d8d8d,#b9b9b9)}
.hero-copy{position:absolute;left:470px;top:70px;width:220px}
.hero-copy h1{font-size:30px;font-weight:700;line-height:1.05;color:#222}
.hero-copy p{font-size:8px;color:#555;margin:10px 0 14px;text-transform:uppercase}
.hero-more{display:inline-block;background:var(--orange);color:#fff;font-family:"Oswald",sans-serif;font-size:9px;padding:5px 14px}
.hero-arrow{position:absolute;top:120px}
.hero-arrow.left{left:110px}.hero-arrow.right{right:20px}

/* welcome */
.welcome{position:absolute;top:392px;left:0;width:756px;text-align:center}
.welcome h2{font-size:15px;font-weight:500;color:var(--teal)}
.welcome h2 em{font-style:normal;color:var(--orange)}
.rule{width:60px;height:2px;background:var(--orange);margin:6px auto 8px}
.welcome p{width:460px;margin:0 auto;color:var(--muted);font-size:8px}

/* services */
.services{position:absolute;top:505px;left:95px;width:566px;display:flex;justify-content:space-between}
.service{width:100px;text-align:center}
.service svg{display:block;margin:0 auto 8px}
.service span{font-family:"Oswald",sans-serif;font-size:8.5px;text-transform:uppercase;color:#444;line-height:1.3;display:block}

/* why */
.why{position:absolute;top:672px;left:0;width:756px;height:200px}
.why-copy{position:absolute;left:40px;top:0;width:300px}
.why-copy h2{font-size:15px;font-weight:500;color:var(--teal)}
.why-copy h2 em{font-style:normal;color:var(--orange)}
.why-copy .rule{margin:6px 0 10px}
.why-copy .lead{color:var(--teal);font-size:10px;margin-bottom:10px}
.why-copy p{color:var(--muted);font-size:8px}
.why-photo{position:absolute;left:360px;top:-10px;width:356px;height:200px;background:linear-gradient(135deg,#d9d9d9,#a8a8a8)}

/* lower */
.lower{position:absolute;top:880px;left:0;width:756px;height:156px;background:var(--panel)}
.col-title{font-family:"Oswald",sans-serif;font-size:11px;color:var(--teal);text-transform:uppercase;border-bottom:1px solid #d5d5d5;padding-bottom:4px;margin-bottom:10px}
.testimonials{position:absolute;left:40px;top:10px;width:300px}
.quote{background:#fff;border:1px solid #ddd;padding:8px 12px;color:var(--muted);font-size:8px;text-align:center}
.person{text-align:center;margin-top:6px;line-height:1.3}
.avatar{width:26px;height:26px;margin:0 auto 3px;background:#b7b7b7}
.person b{font-size:8px;display:block}
.person small{font-size:7px;color:var(--muted);display:block}
.blog{position:absolute;left:370px;top:10px;width:346px}
.posts{display:flex;gap:10px}
.post{width:79px}
.post-thumb{height:44px;background:linear-gradient(135deg,#bdbdbd,#8e8e8e);margin-bottom:4px}
.post b{font-size:7.5px;display:block;line-height:1.3}
.post small{font-size:6.5px;color:var(--muted)}

/* partners */
.partners{position:absolute;top:1046px;left:40px;width:676px;display:flex;justify-content:space-between;align-items:center}
.badge{width:90px;height:28px;border-radius:3px}

/* footer */
.site-footer{position:absolute;top:1100px;left:0;width:756px;height:100px;background:var(--teal)}
.footer-brand{position:absolute;left:288px;top:-18px;width:180px;height:52px;background:#fff;display:flex;align-items:center;justify-content:center}
.footer-brand .brand-name{font-size:14px}
.footer-links{position:absolute;left:40px;top:48px;color:#dff;font-size:7.5px;width:220px}
.footer-links a{color:#fff;text-decoration:none;margin-right:8px}
.footer-legal{position:absolute;right:40px;top:48px;color:#dff;font-size:7.5px;width:220px;text-align:right}
</style>
</head>
<body>

<header class="site-header">
  <div class="brand">
    <span class="brand-name">Trobanex Translations</span>
  </div>
  <div class="top-actions">
    <span class="btn-blue">Upload file</span>
    <span class="btn-orange">Get a quote</span>
  </div>
  <nav class="main-nav">
    <a class="active" href="#">Home</a><a href="#">About us</a><a href="#">Services</a><a href="#">Language</a><a href="#">Stories</a><a href="#">Blog</a><a href="#">Contact us</a>
  </nav>
</header>

<section class="hero">
  <div class="hero-photo" role="img" aria-label="Business team of translators working at a desk with laptops"></div>
  <svg class="hero-arrow left" width="16" height="30" viewBox="0 0 16 30"><path d="M13 2 L3 15 L13 28" stroke="#fff" stroke-width="2" fill="none"/></svg>
  <svg class="hero-arrow right" width="16" height="30" viewBox="0 0 16 30"><path d="M3 2 L13 15 L3 28" stroke="#888" stroke-width="2" fill="none"/></svg>
  <div class="hero-copy">
    <h1 class="heading">Professional<br>Translators</h1>
    <p>Lorem ipsum dolor sit amet consectetur adipiscing elit nullam translations</p>
    <span class="hero-more">MORE ›</span>
  </div>
</section>

<section class="welcome">
  <h2 class="heading">Welcome to <em>Trobanex</em> Translations Agency</h2>
  <div class="rule"></div>
  <p>Lorem ipsum dolor sit amet, consectetur adipiscing elit. Pellentesque pellentesque tempor adipiscing lacus quam in magna viverra vestibulum. Donec adipiscing eget arcu vel adipiscing. Phasellus at volutpat leo, ut commodo nulla.</p>
</section>

<section class="services">
  <div class="service">
    <svg width="62" height="70" viewBox="0 0 62 70"><polygon points="31,2 59,18 59,52 31,68 3,52 3,18" fill="var(--orange)"/><path d="M20 46 L34 32 M30 24 L42 36 M27 27 L39 39" stroke="#fff" stroke-width="4" stroke-linecap="round"/></svg>
    <span>Legal<br>Translations</span>
  </div>
  <div class="service">
    <svg width="62" height="70" viewBox="0 0 62 70"><polygon points="31,2 59,18 59,52 31,68 3,52 3,18" fill="var(--orange-soft)"/><rect x="20" y="38" width="5" height="10" fill="#fff"/><rect x="28" y="30" width="5" height="18" fill="#fff"/><rect x="36" y="23" width="5" height="25" fill="#fff"/></svg>
    <span>Financial<br>Translations</span>
  </div>
  <div class="service">
    <svg width="62" height="70" viewBox="0 0 62 70"><polygon points="31,2 59,18 59,52 31,68 3,52 3,18" fill="var(--amber)"/><path d="M31 48 C14 36 20 22 31 30 C42 22 48 36 31 48Z" fill="#fff"/></svg>
    <span>Healthcare<br>Translations</span>
  </div>
  <div class="service">
    <svg width="62" height="70" viewBox="0 0 62 70"><polygon points="31,2 59,18 59,52 31,68 3,52 3,18" fill="var(--green)"/><rect x="18" y="24" width="26" height="20" rx="2" fill="none" stroke="#fff" stroke-width="3"/><path d="M24 34 L29 39 L38 29" stroke="#fff" stroke-width="3" fill="none"/></svg>
    <span>Audit<br>Translations</span>
  </div>
  <div class="service">
    <svg width="62" height="70" viewBox="0 0 62 70"><polygon points="31,2 59,18 59,52 31,68 3,52 3,18" fill="var(--teal)"/><circle cx="31" cy="35" r="11" fill="none" stroke="#fff" stroke-width="3"/><circle cx="31" cy="35" r="4" fill="#fff"/></svg>
    <span>Corporate<br>Translations</span>
  </div>
</section>

<section class="why">
  <div class="why-copy">
    <h2 class="heading"><em>Why</em> choose us?</h2>
    <div class="rule"></div>
    <p class="lead">Lorem ipsum dolor sit amet, consectetur adipiscing elit. Donec consequat vel amet at facilisis.</p>
    <p>Lorem ipsum dolor sit amet, consectetur adipiscing elit. In ut dictum nisl. In tristique vulputate nisl, eget feugiat mi luctus vel. Aenean pulvinar sem a risus tempus, sit amet mattis lorem commodo. Nulla lobortis metus et felis ultricies, nec egestas quam vulputate. Curabitur facilisis ipsum ante, quis dignissim eros accumsan in. Vivamus convallis nisi sed efficitur tempor nec.</p>
  </div>
  <div class="why-photo" role="img" aria-label="Business people shaking hands in an office"></div>
</section>

<section class="lower">
  <div class="testimonials">
    <div class="col-title">Testimonials</div>
    <div class="quote">“Lorem ipsum dolor sit amet, consectetur adipiscing elit. Donec vitae lorem nec elit fermentum finibus at quis dui.”</div>
    <div class="person">
      <div class="avatar" role="img" aria-label="Client portrait"></div>
      <b>Dana Morel</b>
      <small>Corporate Director</small>
    </div>
  </div>
  <div class="blog">
    <div class="col-title">Latest Blog</div>
    <div class="posts">
      <div class="post"><div class="post-thumb" role="img" aria-label="Team meeting photo"></div><b>Quality in every word</b><small>10.06.2015</small></div>
      <div class="post"><div class="post-thumb" role="img" aria-label="Office workers photo"></div><b>We went to Berlin</b><small>10.06.2015</small></div>
      <div class="post"><div class="post-thumb" role="img" aria-label="Conference photo"></div><b>New healthcare team</b><small>10.06.2015</small></div>
      <div class="post"><div class="post-thumb" role="img" aria-label="Group of colleagues photo"></div><b>Legal language tips</b><small>10.06.2015</small></div>
    </div>
  </div>
</section>

<section class="partners" aria-label="Partners">
  <div class="badge" style="background:#1c6fb8"></div>
  <div class="badge" style="background:#d9d9d9"></div>
  <div class="badge" style="background:#2a2a2a"></div>
  <div class="badge" style="background:#e6e6e6"></div>
  <div class="badge" style="background:#1a8fc9"></div>
  <div class="badge" style="background:#2b9bd6"></div>
</section>

<footer class="site-footer">
  <div class="footer-brand">
    <span class="brand-name">Trobanex Translations</span>
  </div>
  <div class="footer-links">
    <a href="#">Home</a><a href="#">About Us</a><a href="#">Services</a><a href="#">Language</a><br>
    <a href="#">Stories</a><a href="#">Blog</a><a href="#">Contact Us</a>
  </div>
  <div class="footer-legal">© 2015 Trobanex Translations. All rights reserved.<br>Privacy Policy · Terms of Use</div>
</footer>

</body>
</html>
```